Website for Trayvora.net - a web site to market and sell our online school lunch ordering system.

We need a web site to market and engage our online school lunch ordering software. Caterers all over United States are looking for a software that helps them grow by replacing paper based systems with online ordering systems that parents can use to place lunch orders for their kids. Our mobile app compliments our web app by giving parents the freedom to order when they are not in front of their computers or at home. We would like to see designs that can engage our prospects by telling a compelling story about our product with features, metrics, product tours and screenshots.

```html
<!DOCTYPE html>
<html lang="en">
<head>
<meta charset="utf-8">
<title>Trayvora – School Lunch Ordering</title>
<link href="https://fonts.googleapis.com/css2?family=Quicksand:wght@500;600;700&family=Lato:wght@400;700&display=swap" rel="stylesheet">
<style>
:root{
  --yellow:#fcc52c;
  --blue:#5689f6;
  --green:#38cf5a;
  --ink:#2b2b2b;
  --muted:#666;
  --grey-panel:#f2f1ee;
  --white:#fff;
}
*{box-sizing:border-box;margin:0;padding:0}
html,body{width:1200px;height:2350px;overflow:hidden;background:var(--white)}
body{position:relative;font-family:'Lato',sans-serif;color:var(--ink)}
.abs{position:absolute}
.heading{font-family:'Quicksand',sans-serif}

/* hero */
.hero{left:0;top:0;width:1200px;height:600px}
.hero svg{position:absolute;left:0;top:0}
.brand{left:248px;top:60px;color:var(--white)}
.brand-name{font-family:'Quicksand',sans-serif;font-weight:700;font-size:29px;line-height:1}
.brand-sub{font-family:'Quicksand',sans-serif;font-weight:700;font-size:10px;margin-top:3px}
.nav{left:603px;top:66px;display:flex;align-items:center;gap:22px;font-family:'Quicksand',sans-serif;font-size:12.5px;color:var(--white)}
.nav .active{font-weight:700}
.btn-green{background:var(--green);color:var(--white);border-radius:4px;font-family:'Quicksand',sans-serif;font-weight:700;font-size:12px;display:inline-flex;align-items:center;justify-content:center}
.nav .btn-green{width:80px;height:27px}
.hero-title{left:248px;top:192px;width:400px;font-family:'Quicksand',sans-serif;font-weight:700;font-size:28px;line-height:35px;color:var(--white)}
.hero-text{left:248px;top:310px;width:280px;font-size:11px;line-height:15px;color:var(--white)}
.hero .read-more{position:absolute;left:248px;top:357px;width:71px;height:27px}

/* features */
.section-title{left:0;width:1200px;text-align:center;font-family:'Quicksand',sans-serif;font-weight:700;font-size:30px}
.feature{width:240px;text-align:center}
.feature-icon{width:104px;height:104px;border-radius:50%;margin:0 auto;display:flex;align-items:center;justify-content:center}
.feature-icon.yellow{background:var(--yellow)}
.feature-icon.blue{background:var(--blue)}
.feature-icon.green{background:var(--green)}
.feature-title{font-family:'Quicksand',sans-serif;font-weight:700;font-size:15px;margin-top:20px}
.feature-text{font-size:11px;line-height:14.5px;color:var(--muted);margin-top:10px}
.dots{left:577px;top:1201px;display:flex;gap:6px}
.dots span{width:20px;height:4px;border-radius:2px;background:#999}
.dots span.on{background:var(--green)}

/* app band */
.band{left:0;top:1250px;width:1200px;height:420px}
.band svg{position:absolute;left:0;top:0}
.band-title{left:484px;top:1351px;font-family:'Quicksand',sans-serif;font-weight:700;font-size:14.5px;color:var(--white)}
.band-sub{left:484px;top:1375px;font-size:11px;color:var(--white)}
.store-badge{top:1412px;width:127px;height:42px;border-radius:6px;background:#111;border:1px solid #888}
.check-list{top:1482px;list-style:none;font-size:11px;color:var(--white)}
.check-list li{height:24px;display:flex;align-items:center;gap:10px}
.check-list svg{flex:none}

/* stats */
.stat{width:240px;text-align:center}
.stat-label{font-size:14px;color:#888;margin-top:14px}
.stat-num{font-family:'Quicksand',sans-serif;font-weight:700;font-size:35px;line-height:40px;margin-top:2px}
.stat-num.yellow{color:var(--yellow)}
.stat-num.blue{color:var(--blue)}
.stat-num.green{color:var(--green)}

/* footer */
.footer-bg{left:0;top:1990px}
.footer-brand{left:248px;top:2070px;color:var(--ink)}
.footer-brand .brand-name{font-size:27px;font-weight:600}
.footer-brand .brand-sub{font-size:10px}
.contact{left:490px;top:2072px}
.contact h3,.form-box h3{font-family:'Quicksand',sans-serif;font-weight:600;font-size:15px}
.contact-line{display:flex;gap:8px;font-size:11px;line-height:14px;color:#444;margin-top:16px}
.form-box{left:675px;top:2072px;width:276px}
.field{position:absolute;background:var(--white);border:1px solid #ccc;border-radius:4px;font-size:8px;color:#555;padding:6px 8px}
.form-box .submit{position:absolute;left:0;top:183px;width:59px;height:19px;font-size:9px;border-radius:3px}
.legal{left:248px;top:2308px;font-size:9px;color:#444;display:flex;gap:14px}
</style>
</head>
<body>

<section class="abs hero">
  <svg width="1200" height="600" viewBox="0 0 1200 600">
    <defs>
      <linearGradient id="kidsTone" x1="0" y1="0" x2="1" y2="1">
        <stop offset="0" stop-color="#5d6b76"/>
        <stop offset="0.5" stop-color="#a7b7c0"/>
        <stop offset="1" stop-color="#6f7d86"/>
      </linearGradient>
      <linearGradient id="foodTone" x1="0" y1="0" x2="1" y2="1">
        <stop offset="0" stop-color="#6b4a2c"/>
        <stop offset="0.55" stop-color="#d89a3a"/>
        <stop offset="1" stop-color="#f1c76a"/>
      </linearGradient>
    </defs>
    <rect width="1200" height="600" fill="url(#kidsTone)" role="img" aria-label="Photo of three smiling school children holding phones"/>
    <polygon points="0,330 700,400 690,530 0,580" fill="url(#foodTone)" role="img" aria-label="Photo of a burger with fries on a plate"/>
    <polygon points="0,0 556,0 680,418 0,332" fill="var(--yellow)"/>
    <polygon points="0,588 690,518 1200,595 1200,600 0,600" fill="var(--white)"/>
  </svg>
  <div class="abs brand">
    <div class="brand-name">Trayvora</div>
    <div class="brand-sub">Brightfield Software LLC Food &amp; Drink</div>
  </div>
  <nav class="abs nav">
    <span class="active">Pricing</span>
    <span>Product Features</span>
    <span>Request a Demo</span>
    <span class="btn-green">Contact Us</span>
  </nav>
  <h1 class="abs hero-title">You Can Place School Lunch Orders Right From Your Phone.</h1>
  <p class="abs hero-text">Lorem Ipsum is simply dummy text of the printing and typesetting industry.</p>
  <span class="btn-green read-more">Read More</span>
</section>

<h2 class="abs section-title" style="top:596px">Product Features</h2>

<div class="abs feature" style="left:240px;top:674px">
  <div class="feature-icon yellow"><svg width="44" height="44" viewBox="0 0 44 44" fill="#fff"><rect x="2" y="2" width="11" height="11"/><rect x="16.5" y="2" width="11" height="11"/><rect x="31" y="2" width="11" height="11"/><rect x="2" y="16.5" width="11" height="11"/><rect x="16.5" y="16.5" width="11" height="11"/><rect x="31" y="16.5" width="11" height="11"/><rect x="2" y="31" width="11" height="11"/><rect x="16.5" y="31" width="11" height="11"/><rect x="31" y="31" width="11" height="11"/></svg></div>
  <div class="feature-title">Advanced Menu Builder</div>
  <p class="feature-text">Easy to use drag and drop Menu Builder. Share Menu items across multiple schools using a Master Template. Specify exclusions at School level for overrides.</p>
</div>
<div class="abs feature" style="left:480px;top:674px">
  <div class="feature-icon blue"><svg width="60" height="44" viewBox="0 0 60 44"><text x="30" y="33" text-anchor="middle" font-family="Lato,sans-serif" font-weight="700" fill="#fff"><tspan font-size="18">$</tspan><tspan font-size="22">$</tspan><tspan font-size="34">$</tspan></text></svg></div>
  <div class="feature-title">Flexible Pricing</div>
  <p class="feature-text">Flexible pricing options for your menu.<br>Configure prices by school<br>or by portion size.</p>
</div>
<div class="abs feature" style="left:721px;top:674px">
  <div class="feature-icon green"><svg width="36" height="44" viewBox="0 0 36 44" fill="none" stroke="#fff" stroke-width="4"><rect x="3" y="6" width="30" height="36" rx="2"/><rect x="11" y="2" width="14" height="8" fill="#fff"/><line x1="10" y1="20" x2="26" y2="20"/><line x1="10" y1="28" x2="26" y2="28"/><line x1="10" y1="35" x2="20" y2="35"/></svg></div>
  <div class="feature-title">Automated Ordering</div>
  <p class="feature-text">Parents can set up item favorites and let Trayvora do the item selection based on selected favorites and item availability. Parents love this feature.</p>
</div>

<div class="abs feature" style="left:240px;top:931px">
  <div class="feature-icon yellow"><svg width="30" height="50" viewBox="0 0 30 50"><rect x="2" y="2" width="26" height="46" rx="4" fill="none" stroke="#fff" stroke-width="3"/><rect x="9" y="18" width="12" height="12" fill="#fff" transform="rotate(45 15 24)"/><circle cx="15" cy="42" r="2" fill="#fff"/></svg></div>
  <div class="feature-title">Mobile App</div>
  <p class="feature-text">Our Mobile app is available for all phone and tablet devices. Parents can place new orders and manage existing orders using our app. Use our app's notification feature to remind customers about ordering deadlines.</p>
</div>
<div class="abs feature" style="left:480px;top:931px">
  <div class="feature-icon blue"><svg width="46" height="46" viewBox="0 0 46 46" stroke="#fff" stroke-width="5" stroke-linecap="round"><line x1="8" y1="8" x2="38" y2="40"/><line x1="38" y1="6" x2="8" y2="40"/></svg></div>
  <div class="feature-title">Free &amp; Reduced</div>
  <p class="feature-text">Support for Free &amp; Reduced meal program. Caterers can set up F/R students and customize meal pricing for their F/R program including qty restrictions.</p>
</div>
<div class="abs feature" style="left:721px;top:931px">
  <div class="feature-icon green"><svg width="44" height="40" viewBox="0 0 44 40" fill="#fff"><polygon points="22,4 42,38 2,38"/><polygon points="22,22 28,38 16,38" fill="var(--green)"/><rect x="21" y="0" width="2" height="6"/></svg></div>
  <div class="feature-title">Camps</div>
  <p class="feature-text">Caterers can set up advanced configuration for their meal programs to Summer camps. Customize the store cart to let you invoice the school instead of parents paying for their lunch orders.</p>
</div>

<div class="abs dots"><span class="on"></span><span></span></div>

<section class="abs band">
  <svg width="1200" height="420" viewBox="0 0 1200 420">
    <defs>
      <linearGradient id="lunchTone" x1="0" y1="0" x2="1" y2="1">
        <stop offset="0" stop-color="#c9b79a"/>
        <stop offset="0.5" stop-color="#e6a9b5"/>
        <stop offset="1" stop-color="#8a7f6c"/>
      </linearGradient>
      <linearGradient id="screenTone" x1="0" y1="0" x2="0" y2="1">
        <stop offset="0" stop-color="#ecf8ef"/>
        <stop offset="1" stop-color="#ffffff"/>
      </linearGradient>
    </defs>
    <polygon points="0,8 1200,38 1200,360 0,402" fill="var(--green)"/>
    <polygon points="190,370 995,380 995,420 190,420" fill="var(--grey-panel)"/>
    <polygon points="825,30 1200,22 1200,365 783,385" fill="url(#lunchTone)" role="img" aria-label="Photo of children being served lunch in a school cafeteria"/>
    <rect x="258" y="10" width="197" height="395" rx="30" fill="#f4f1ea" stroke="#d8cfbd" stroke-width="3"/>
    <rect x="270" y="57" width="173" height="298" fill="url(#screenTone)" stroke="#ccc" role="img" aria-label="Screenshot of the parent ordering app listing children with order buttons"/>
    <rect x="270" y="57" width="173" height="14" fill="var(--green)"/>
    <rect x="270" y="340" width="173" height="15" fill="var(--green)"/>
    <rect x="335" y="30" width="44" height="4" rx="2" fill="#bbb"/>
    <circle cx="357" cy="379" r="14" fill="none" stroke="#cfc6b4" stroke-width="2"/>
  </svg>
</section>
<p class="abs band-title">Lorem Ipsum is simply dummy of the printing</p>
<p class="abs band-sub">Lorem Ipsum is simply dummy text of the printing.</p>
<span class="abs store-badge" style="left:484px"></span>
<span class="abs store-badge" style="left:622px"></span>
<ul class="abs check-list" style="left:486px">
  <li><svg width="7" height="10" viewBox="0 0 7 10"><polyline points="1,1 5,5 1,9" fill="none" stroke="#fff" stroke-width="1.6"/></svg>Lorem Ipsum is simply.</li>
  <li><svg width="7" height="10" viewBox="0 0 7 10"><polyline points="1,1 5,5 1,9" fill="none" stroke="#fff" stroke-width="1.6"/></svg>Lorem Ipsum is simply.</li>
  <li><svg width="7" height="10" viewBox="0 0 7 10"><polyline points="1,1 5,5 1,9" fill="none" stroke="#fff" stroke-width="1.6"/></svg>Lorem Ipsum is simply.</li>
</ul>
<ul class="abs check-list" style="left:646px">
  <li><svg width="7" height="10" viewBox="0 0 7 10"><polyline points="1,1 5,5 1,9" fill="none" stroke="#fff" stroke-width="1.6"/></svg>Lorem Ipsum is simply.</li>
  <li><svg width="7" height="10" viewBox="0 0 7 10"><polyline points="1,1 5,5 1,9" fill="none" stroke="#fff" stroke-width="1.6"/></svg>Lorem Ipsum is simply.</li>
  <li><svg width="7" height="10" viewBox="0 0 7 10"><polyline points="1,1 5,5 1,9" fill="none" stroke="#fff" stroke-width="1.6"/></svg>Lorem Ipsum is simply.</li>
</ul>

<svg class="abs" style="left:0;top:1660px" width="1200" height="280" viewBox="0 0 1200 280">
  <polygon points="190,0 995,0 995,258 205,265" fill="var(--grey-panel)"/>
  <polygon points="205,265 995,252 995,262 205,274" fill="var(--green)"/>
</svg>

<div class="abs stat" style="left:240px;top:1700px">
  <svg width="84" height="72" viewBox="0 0 84 72" fill="var(--yellow)"><rect x="4" y="18" width="26" height="22"/><circle cx="44" cy="10" r="7"/><path d="M38 20h12l6 18h14v8H30v-8h12z"/><circle cx="22" cy="56" r="10"/><circle cx="66" cy="56" r="10"/><circle cx="22" cy="56" r="4" fill="var(--grey-panel)"/><circle cx="66" cy="56" r="4" fill="var(--grey-panel)"/></svg>
  <div class="stat-label"># of Orders Served</div>
  <div class="stat-num yellow">300K +</div>
</div>
<div class="abs stat" style="left:480px;top:1700px">
  <svg width="100" height="72" viewBox="0 0 100 72" fill="var(--blue)"><circle cx="50" cy="36" r="28"/><circle cx="50" cy="36" r="19" fill="var(--grey-panel)"/><circle cx="50" cy="36" r="15"/><rect x="8" y="6" width="5" height="62" rx="2"/><path d="M87 6c8 4 8 22 2 28v34h-5V6z"/></svg>
  <div class="stat-label"># of Meals served</div>
  <div class="stat-num blue">1.5 million +</div>
</div>
<div class="abs stat" style="left:721px;top:1700px">
  <svg width="60" height="72" viewBox="0 0 60 72"><path d="M22 14a8 8 0 0 1 16 0" fill="none" stroke="var(--green)" stroke-width="4"/><rect x="6" y="14" width="48" height="54" rx="12" fill="var(--green)"/><rect x="16" y="38" width="28" height="18" rx="3" fill="none" stroke="var(--grey-panel)" stroke-width="3"/><line x1="16" y1="46" x2="44" y2="46" stroke="var(--grey-panel)" stroke-width="3"/></svg>
  <div class="stat-label"># of Schools/ Camps</div>
  <div class="stat-num green">1000+</div>
</div>

<svg class="abs footer-bg" width="1200" height="360" viewBox="0 0 1200 360">
  <polygon points="0,0 1200,40 1200,360 0,360" fill="var(--grey-panel)"/>
</svg>

<div class="abs footer-brand">
  <div class="brand-name">Trayvora</div>
  <div class="brand-sub">Brightfield Software LLC Food &amp; Drink</div>
</div>

<div class="abs contact">
  <h3>Contact Us</h3>
  <div class="contact-line">
    <svg width="10" height="14" viewBox="0 0 10 14"><path d="M5 0a5 5 0 0 1 5 5c0 4-5 9-5 9S0 9 0 5a5 5 0 0 1 5-5z" fill="var(--green)"/><circle cx="5" cy="5" r="2" fill="#fff"/></svg>
    <span>Trayvora<br>215 Orchard Lane # 102<br>Millbrook, CA 94010</span>
  </div>
  <div class="contact-line">
    <svg width="12" height="12" viewBox="0 0 12 12"><path d="M2 0l3 3-1.5 1.5a7 7 0 0 0 4 4L9 7l3 3-2 2C5 12 0 7 0 2z" fill="var(--green)"/></svg>
    <span>555 014 2290</span>
  </div>
</div>

<form class="abs form-box">
  <h3>Form for requesting more information.</h3>
  <div class="field" style="left:0;top:38px;width:276px;height:24px">Contact Name (Required)</div>
  <div class="field" style="left:0;top:71px;width:134px;height:24px">Email (Required)</div>
  <div class="field" style="left:142px;top:71px;width:134px;height:24px">Phone # (optional)</div>
  <div class="field" style="left:0;top:104px;width:276px;height:70px">Message</div>
  <span class="btn-green submit">Submit</span>
</form>

<div class="abs legal">
  <span>2018 Trayvora. All Rights Reserved.</span><span>I</span><span>Terms of Usage</span><span>I</span><span>Privacy Policy</span>
</div>

</body>
</html>
```